DM - management consultant

Business card - contemporary design

Front info
Dorian Maples

(Address not necessary)
PO Box 7386
Belmont, CA 94002

(650) 555-0143
dm@dorianmapl.es

Twitter: dmq527
Facebook: /Dorian.Maples
Linkedin: /in/dorianmaples

Back or Front
www.dorianmaples.net
Facilitation & coaching, change management, strategic partnerships, business improvement

Target Market(s)

High tech businesses - mostly startups in Silicon Valley

Industry/Entity Type

Business

Font styles to use
Sans Serif

Colors

Designer to choose colors to be used in the design.

```html
<!DOCTYPE html>
<html lang="en">
<head>
<meta charset="utf-8">
<title>Dorian Maples – Business Card</title>
<link href="https://fonts.googleapis.com/css2?family=Source+Sans+3:wght@400;600&display=swap" rel="stylesheet">
<style>
  :root {
    --page-bg: #d5d6d8;
    --card-bg: #ffffff;
    --brand-blue: #0a87c7;
    --text-blue: #1b8fd0;
    --ink: #111111;
    --muted: #555a60;
    --pattern-light: #e4e6e8;
    --pattern-dark: #50555a;
    --on-blue: #ffffff;
  }
  * { margin: 0; padding: 0; box-sizing: border-box; }
  html, body {
    width: 1200px; height: 1200px; overflow: hidden;
    background: var(--page-bg);
    font-family: "Source Sans 3", sans-serif;
  }
  .canvas { position: relative; width: 1200px; height: 1200px; }
  .card {
    position: absolute; left: 228px; width: 744px;
    background: var(--card-bg); overflow: hidden;
  }
  .card--front { top: 170px; height: 424px; }
  .card--back { top: 596px; height: 426px; }

  .mark {
    position: absolute; display: flex; align-items: center;
    color: var(--brand-blue); font-weight: 600; line-height: 1;
  }
  .mark__dot { border-radius: 50%; background: var(--brand-blue); flex: none; }
  .mark--small { left: 40px; top: 62px; font-size: 56px; gap: 10px; }
  .mark--small .mark__dot { width: 18px; height: 18px; }
  .mark--large { left: 120px; top: 160px; font-size: 150px; gap: 18px; }
  .mark--large .mark__dot { width: 40px; height: 40px; }

  .role {
    position: absolute; left: 98px; top: 130px;
    font-size: 19px; color: var(--muted);
  }
  .name {
    position: absolute; left: 463px; top: 115px;
    font-size: 26px; font-weight: 600; color: var(--brand-blue);
  }
  .contact {
    position: absolute; left: 463px; top: 236px;
    font-size: 18px; line-height: 24px; color: var(--ink);
    list-style: none;
  }
  .band {
    position: absolute; left: 0; top: 300px; width: 744px; height: 121px;
    background: var(--brand-blue);
  }
  .band__pattern {
    position: absolute; left: 0; top: 28px; width: 324px; height: 93px;
    background: linear-gradient(90deg, var(--pattern-light), #c9d8e3);
    opacity: 0.9;
  }
  .social {
    position: absolute; left: 463px; top: 4px;
    font-size: 18px; line-height: 24px; color: var(--on-blue);
    list-style: none;
  }
  .social__web { margin-top: 10px; }

  .back-web {
    position: absolute; left: 132px; top: 14px;
    font-size: 18px; color: var(--ink);
  }
  .back-pattern {
    position: absolute; left: 424px; top: 6px; width: 320px; height: 94px;
    background: var(--pattern-dark);
  }
  .services {
    position: absolute; left: 302px; top: 346px;
    font-size: 19px; line-height: 22px; color: var(--text-blue);
  }
</style>
</head>
<body>
<div class="canvas">
  <section class="card card--front">
    <div class="mark mark--small"><span class="mark__dot"></span><span>DM</span></div>
    <p class="role">Management Consultant</p>
    <h1 class="name">Dorian Maples</h1>
    <ul class="contact">
      <li>Phone: (650) 555-0143</li>
      <li>Mail: dm@dorianmapl.es</li>
    </ul>
    <div class="band">
      <div class="band__pattern" role="img" aria-label="Checkerboard of light rounded squares"></div>
      <ul class="social">
        <li>Twitter: dmq527</li>
        <li>Facebook: /Dorian.Maples</li>
        <li>Linkedin: /in/dorianmaples</li>
        <li class="social__web">www.dorianmaples.net</li>
      </ul>
    </div>
  </section>

  <section class="card card--back">
    <p class="back-web">www.dorianmaples.net</p>
    <div class="back-pattern" role="img" aria-label="Checkerboard of dark grey rounded squares"></div>
    <div class="mark mark--large"><span>DM</span><span class="mark__dot"></span></div>
    <p class="services">Facilitation &amp; coaching, Change management<br>Strategic partnerships, Business improvement</p>
  </section>
</div>
</body>
</html>
```